Business Card Design

Electronic Security
Alarm Systems
CCTV
Electronic Access Control
Security System Integration

Industry/Entity Type

Business

Contact Information for Business Card

Declan Whitfield
PO Box 862
Carrowbrook Qld 4179
Phone 07 38265014
Mob 0428615937

```html
<!DOCTYPE html>
<html lang="en">
<head>
<meta charset="utf-8">
<title>Halvern – Business Card</title>
<link href="https://fonts.googleapis.com/css2?family=Arimo:wght@400;700&display=swap" rel="stylesheet">
<style>
  :root {
    --page: #e9e7e4;
    --card: #ffffff;
    --ink: #111111;
    --accent-orange: #f39a1e;
    --accent-blue: #1f8fd6;
    --rule: #222222;
  }
  * { box-sizing: border-box; margin: 0; padding: 0; }
  html, body {
    width: 1200px; height: 960px; overflow: hidden;
    background: var(--page);
    font-family: "Arimo", Arial, sans-serif;
    color: var(--ink);
  }
  .stage {
    width: 1200px; height: 960px;
    display: flex; align-items: center; justify-content: center;
  }
  .card {
    position: relative;
    width: 840px; height: 480px;
    background: var(--card);
    box-shadow: 0 10px 30px rgba(0,0,0,0.18);
  }
  .brand {
    position: absolute; top: 62px; right: 70px;
    display: flex; align-items: center; gap: 18px;
  }
  .brand-mark {
    width: 30px; height: 30px; border-radius: 50%;
    background: var(--accent-orange);
  }
  .brand-name {
    font-size: 64px; font-weight: 400; letter-spacing: 1px;
    color: var(--ink); line-height: 1;
  }
  .brand-divider {
    width: 2px; height: 70px; background: var(--rule);
  }
  .brand-tagline {
    font-size: 15px; line-height: 1.05; font-weight: 400;
  }
  .services {
    position: absolute; top: 178px; left: 96px;
    font-size: 27px; line-height: 1.08;
  }
  .holder {
    position: absolute; top: 300px; left: 62px;
    font-size: 29px; font-weight: 700;
  }
  .contacts {
    position: absolute; top: 352px; left: 62px;
    list-style: none; font-size: 23px; line-height: 1.28;
  }
  .contacts li { display: flex; align-items: center; gap: 14px; }
  .contacts svg { width: 18px; height: 18px; flex: none; }
</style>
</head>
<body>
<main class="stage">
  <section class="card">
    <header class="brand">
      <span class="brand-mark" aria-hidden="true"></span>
      <span class="brand-name">Halvern</span>
      <span class="brand-divider" aria-hidden="true"></span>
      <span class="brand-tagline">Halvern<br>Electronic<br>Security</span>
    </header>

    <p class="services">
      Electronic Security, Alarm Systems<br>
      CCTV, Electronic Access Control<br>
      Security System Integration
    </p>

    <h1 class="holder">Declan Whitfield</h1>

    <ul class="contacts">
      <li>
        <svg viewBox="0 0 18 18" aria-label="Mobile"><rect x="3" y="1.5" width="12" height="15" rx="2" fill="none" stroke="#111" stroke-width="2"/></svg>
        0428615937
      </li>
      <li>
        <svg viewBox="0 0 18 18" aria-label="Phone"><path d="M4 2 L7 2 L8 6 L6 7.5 C7 10 8.5 11.5 10.5 12 L12 10 L16 11 L16 14 C16 15 15 16 14 16 C8 15.5 2.5 10 2 4 C2 3 3 2 4 2 Z" fill="#111"/></svg>
        07 38265014
      </li>
      <li>
        <svg viewBox="0 0 18 18" aria-label="Address"><path d="M9 1.5 C5.7 1.5 3.5 3.8 3.5 6.8 C3.5 10.5 9 16.5 9 16.5 C9 16.5 14.5 10.5 14.5 6.8 C14.5 3.8 12.3 1.5 9 1.5 Z" fill="#111"/><circle cx="9" cy="6.8" r="2.2" fill="#fff"/></svg>
        PO Box 862 Carrowbrook Qld 4179
      </li>
    </ul>
  </section>
</main>
</body>
</html>
```